Home page redesign for an international job board

Need a modern design based on current structure of the page. I am happy with the current structure and layout/architecture, not entirely happy with how it looks. While I still want to keep most of the elements in place ( especially the search box) I would like to get another look and feel - more appealing to any audience related to online job search

Home page is: www.drumvaliant.ro

Target Market(s)

job seeekers and employers

Industry/Entity Type

Architecture

Number of Pages Required

1 page

Font styles to use
Sans Serif

Colors
33a6d7

Requirements
Must have
• Stay with the same structure: Seach box, latest jobs, articles
Nice to have
• Key element: search for jobs - this needs to be very clear

```html
<!DOCTYPE html>
<html lang="en">
<head>
<meta charset="utf-8">
<title>DrumValiant – Job search</title>
<link href="https://fonts.googleapis.com/css2?family=Open+Sans:wght@400;600;700&display=swap" rel="stylesheet">
<style>
:root{
  --blue:#4a9bc1;
  --blue-dark:#3a88ad;
  --red:#a8080c;
  --red-text:#b00f12;
  --dark:#2d2d2d;
  --ink:#222;
  --muted:#666;
  --light:#f2f2f2;
  --grey:#a5a5a5;
  --white:#fff;
}
*{box-sizing:border-box;margin:0;padding:0}
html,body{width:681px;height:1200px;overflow:hidden}
body{font-family:'Open Sans',sans-serif;color:var(--ink);background:var(--white);position:relative}
.wrap{position:absolute;left:70px;width:540px}
a{color:inherit;text-decoration:none}

.topbar{position:absolute;top:0;left:0;width:681px;height:22px;background:var(--light);font-size:6px}
.topbar .links{top:7px}
.topbar .links span{margin:0 5px;color:#999}
.topbar .lang{position:absolute;right:71px;top:7px;font-weight:700}
.topbar .lang .en{color:var(--red-text)}
.topbar .lang i{color:#bbb;font-style:normal;margin:0 4px;font-weight:400}

.header{position:absolute;top:22px;left:0;width:681px;height:38px}
.brand{position:absolute;left:70px;top:8px;display:flex;align-items:center;gap:4px;font-size:13px;font-weight:600;color:var(--ink)}
.brand .dot{width:20px;height:20px;border-radius:50%;background:var(--red)}
.auth{position:absolute;right:71px;top:11px;display:flex;gap:11px}
.auth a{font-size:8px;color:var(--white);padding:3px 10px;border-radius:2px}
.auth .login{background:var(--blue)}
.auth .register{background:var(--red)}

.nav{position:absolute;top:60px;left:0;width:681px;height:28px;background:var(--dark);display:flex;padding-left:97px}
.nav a{color:var(--white);font-size:8px;font-weight:700;line-height:28px;padding:0 14px;text-transform:uppercase}
.nav a.active{background:var(--blue);padding:0 12px;width:80px;position:relative}
.nav a.active:after{content:"";position:absolute;left:50%;bottom:-5px;margin-left:-5px;border:5px solid transparent;border-bottom:0;border-top-color:var(--blue)}

.hero{position:absolute;top:88px;left:0;width:681px;height:219px;background:linear-gradient(90deg,#8f8f8f 0%,#6d6d6d 40%,#3d3d3d 60%,#777 100%)}
.search{position:absolute;left:70px;top:46px;width:231px}
.field{background:#f4f4f4;border-radius:2px;height:27px;font-size:7px;color:#999;padding:0 9px;line-height:27px;position:relative}
.row{display:flex;gap:4px;margin-top:5px}
.row .field{width:113px}
.field.select:after{content:"";position:absolute;right:9px;top:11px;border:4px solid transparent;border-top:5px solid var(--ink);border-bottom:0}
.btn-search{margin-top:6px;width:113px;height:26px;background:var(--red);color:var(--white);font-weight:700;font-size:11px;text-align:center;line-height:26px;border-radius:2px}
.panel{position:absolute;left:445px;top:18px;width:165px;height:181px;background:rgba(30,30,30,.88);border-radius:2px;padding:11px 11px;color:var(--white)}
.panel h2{font-size:10px;font-weight:400;line-height:13px}
.panel p{font-size:6.6px;line-height:11px;margin-top:8px}
.panel .act{display:flex;align-items:center;gap:6px;margin-top:5px;width:113px;height:17px;background:var(--blue);font-size:6.6px;padding-left:6px;border-radius:1px}
.panel .act:first-of-type{margin-top:11px}
.panel .act svg{width:9px;height:9px}

.jobs{position:absolute;top:307px;left:0;width:681px;height:235px}
.cards{position:absolute;left:70px;top:31px;display:flex;gap:19px}
.card{width:167px;text-align:center}
.card .photo{height:105px;border-radius:1px}
.card h3{font-size:7px;font-weight:700;color:var(--red-text);margin-top:11px}
.card .loc{font-size:7px;color:var(--muted);margin-top:3px}
.card .co{font-size:7px;font-weight:700;margin-top:3px}
.card .more{display:inline-block;margin-top:7px;background:var(--blue);color:var(--white);font-size:6px;font-weight:700;padding:2px 4px}

.articles{position:absolute;top:542px;left:0;width:681px;height:253px;background:var(--grey)}
.articles h2{text-align:center;font-weight:400;color:var(--white);font-size:16px;margin-top:27px}
.articles h2:after{content:"";display:block;width:20px;height:1px;background:var(--white);margin:4px auto 0}
.article{position:absolute;left:70px;top:71px;width:540px;height:132px;background:var(--white);display:flex}
.article .photo{width:225px;height:132px;background:linear-gradient(160deg,#b8dbe0 0%,#2a8a92 45%,#1d5e6e 70%,#a9c3d0 100%)}
.article .body{padding:17px 18px}
.article h3{font-size:7px;color:var(--red-text);font-weight:700}
.article time{font-size:6px;color:#aaa;display:block;margin-top:5px}
.article p{font-size:7px;margin-top:19px}
.shares{display:flex;gap:14px;margin-top:14px;font-size:7px}
.shares span{display:flex;align-items:center;gap:5px}
.shares .b{color:var(--blue)}
.shares .r{color:#d5523e}
.shares i{width:8px;height:8px;background:currentColor;display:inline-block;border-radius:1px}
.dots{position:absolute;top:215px;left:0;width:681px;display:flex;justify-content:center;gap:4px}
.dots b{width:7px;height:7px;border-radius:50%;background:var(--white)}
.dots b.on{background:var(--blue)}

.apps{position:absolute;top:824px;left:70px;display:flex;gap:19px}
.app{width:167px;height:58px;background:var(--blue);display:flex;align-items:center;padding-left:15px;gap:11px;color:var(--white);border-radius:1px}
.app .ic{width:34px;height:34px;border-radius:50%;background:var(--white)}
.app .t{font-size:12px;line-height:15px}
.app .t b{display:block;font-size:15px;font-weight:700}
.app .t b:after{content:" ›";font-size:9px;margin-left:4px}

.intro{position:absolute;top:912px;left:70px;width:540px;border-top:1px solid #eaeaea;text-align:center}
.intro h2{font-size:10px;font-weight:700;margin-top:21px}
.intro p{font-size:7px;line-height:11px;margin-top:9px;padding:0 20px}

.footer{position:absolute;top:1005px;left:0;width:681px;height:150px;background:var(--light)}
.cols{position:absolute;left:70px;top:22px;width:540px;font-size:7px;color:#555}
.col{position:absolute;top:0;line-height:12.6px}
.col h4{font-size:7px;color:var(--ink);font-weight:700;margin-bottom:1px}
.partner{position:absolute;left:469px;top:16px;width:71px;height:52px;border-radius:26px;background:var(--blue-dark)}
.browse{position:absolute;left:70px;top:104px;width:540px;border-top:1px solid #ddd;padding-top:5px;font-size:5.6px;line-height:10.5px;color:#444}
.browse b{color:var(--ink)}
.social{position:absolute;right:71px;top:126px;display:flex;gap:3px}
.social i{width:16px;height:16px;display:block}
.bottom{position:absolute;top:1155px;left:0;width:681px;height:45px;background:#e6e6e6;text-align:center;font-size:6px;color:#555;line-height:14px;padding-top:9px}
</style>
</head>
<body>

<div class="topbar">
  <div class="wrap links">Jobs<span>|</span>Career Coach<span>|</span>Interview Tips</div>
  <div class="lang">RO<i>|</i><span class="en">EN</span></div>
</div>

<header class="header">
  <div class="brand"><span class="dot"></span>DrumValiant</div>
  <div class="auth"><a class="login" href="#">Login</a><a class="register" href="#">Register</a></div>
</header>

<nav class="nav">
  <a class="active" href="#">Search Jobs</a>
  <a href="#">My Account</a>
  <a href="#">Career Counselling</a>
  <a href="#">Features</a>
  <a href="#">Employer &amp; Post a Job</a>
</nav>

<section class="hero" role="img" aria-label="Businessman in glasses using a tablet in an office">
  <form class="search">
    <div class="field">Type Keywords</div>
    <div class="row"><div class="field select">Classification</div><div class="field select">Region</div></div>
    <div class="row"><div class="field select">Work Type</div><div class="field select">Locatie</div></div>
    <div class="btn-search">SEARCH</div>
  </form>
  <aside class="panel">
    <h2>Find jobs, create your jobseeker profile, search jobs your way</h2>
    <p>Create a profile and tell employers about your skills, experience and what you are looking for in your next role</p>
    <div class="act"><svg viewBox="0 0 10 10"><path d="M1 4h5V2l3 3-3 3V6H1z" fill="#fff"/></svg>Post Your Resume</div>
    <div class="act"><svg viewBox="0 0 10 10"><path d="M1 9l8-8M6 1h3v3" stroke="#fff" fill="none"/></svg>Set Your Job Alerts</div>
    <div class="act"><svg viewBox="0 0 10 10"><rect x="1" y="1.5" width="8" height="7" fill="none" stroke="#fff"/><path d="M3 4h4M3 6h4" stroke="#fff"/></svg>Manage Your Job Search</div>
  </aside>
</section>

<section class="jobs">
  <div class="cards">
    <article class="card">
      <div class="photo" role="img" aria-label="Man in a suit in front of bookshelves" style="background:linear-gradient(90deg,#5a3d2a,#2b2320 50%,#6a4a34)"></div>
      <h3>eHEALTH SPECIALIST</h3><div class="loc">London Westmere Health</div><div class="co">Westmere Health</div><a class="more" href="#">READ MORE</a>
    </article>
    <article class="card">
      <div class="photo" role="img" aria-label="Hands pointing at documents on a desk" style="background:linear-gradient(135deg,#c9d3dc,#eef1f4 55%,#aeb8c3)"></div>
      <h3>Application Support Analyst (Support, SQL)</h3><div class="loc">Dorset Pellham Bank</div><div class="co">Pellham Bank</div><a class="more" href="#">READ MORE</a>
    </article>
    <article class="card">
      <div class="photo" role="img" aria-label="Businessman holding a small tree illustration" style="background:radial-gradient(circle at 50% 40%,#e6ebee,#a9b6be)"></div>
      <h3>Lead Functional Test Engineer</h3><div class="loc">Dorset Pellham Bank</div><div class="co">Westmere Health</div><a class="more" href="#">READ MORE</a>
    </article>
  </div>
</section>

<section class="articles">
  <h2>Articles</h2>
  <article class="article">
    <div class="photo" role="img" aria-label="Surfer riding inside a large ocean wave"></div>
    <div class="body">
      <h3>Vicios sau virtuos?</h3>
      <time>11.22.2015</time>
      <p>"Am incercat". "Incerc". "Voi incerca..."&nbsp;&nbsp; Ai simti [...]</p>
      <div class="shares"><span class="b"><i></i>Share</span><span class="b"><i></i>Tweet</span><span class="r"><i></i>Share</span></div>
    </div>
  </article>
  <div class="dots"><b class="on"></b><b></b><b></b></div>
</section>

<section class="apps">
  <a class="app" href="#"><span class="ic"></span><span class="t">Job app for<b>Pocketphone</b></span></a>
  <a class="app" href="#"><span class="ic"></span><span class="t">Job app for<b>Droidon</b></span></a>
  <a class="app" href="#"><span class="ic"></span><span class="t">Job app for<b>Friendly</b></span></a>
</section>

<section class="intro">
  <h2>International careers. Overseas jobs and employment opportunities</h2>
  <p>DrumValiant.ro is a job search and employment resource. For jobseekers we provide jobs from Romanian and International employers and for hiring managers we aim to deliver quality candidates across all fields of expertise.</p>
</section>

<footer class="footer">
  <div class="cols">
    <div class="col" style="left:0"><h4>Connect with us</h4>Friendly<br>Chirper<br>Circlesy<br>Workweb<br>Blog</div>
    <div class="col" style="left:121px"><h4>Go Mobile</h4>Pocketphone App<br>Droidon App<br>Friendly App<br>Mobile Version</div>
    <div class="col" style="left:236px"><h4>Employer Tools</h4>Post job ads<br>Access jobseekers<br>Resume Search<br>Analytics</div>
    <div class="col" style="left:358px"><h4>Job Seeker Tools</h4>Resume Posting<br>Job Alerts<br>Video Resume<br>Create Profile</div>
    <div class="col" style="left:469px"><h4>Our Partners</h4></div>
    <div class="partner"></div>
  </div>
  <div class="browse">
    <b>Browse jobs by:</b><br>
    <b>Classifications:</b> IT_Software Development | Banking | Sales | Medical | Engineering | view all classifications<br>
    <b>Cities:</b> Bucuresti | Cluj-Napoca | Timisoara | Iasi | Constanta | Craiova | Brasov | Galati | Ploiesti | Oradea | Pitesti | Sibiu
  </div>
  <div class="social">
    <i style="background:#1a74b5"></i><i style="background:#e8691d"></i><i style="background:#d8261f"></i><i style="background:#d64434"></i><i style="background:#2aa3e0"></i><i style="background:#355b9e"></i>
  </div>
</footer>

<div class="bottom">About us | Terms and conditions | Privacy Policy | Contact<br>2015 All right Reserved</div>

</body>
</html>
```